Professional Facebook Banner, Business Cards, Door Hang Tags, Service Flyer for Pest Control Company

There are really 4 things I need designed but Pixel Harbor doesn't have them to package together. I am needing to get a Professional Facebook Banner, Business Cards, Door Hang Tags, and Service Flyer for a Pest Control Company. I already have a logo that I will attach to the project along with content a for each one of these tasks. Please see document attached labeled All Design Content & Flyer Content.
Pest Control

```html
<!DOCTYPE html>
<html lang="en">
<head>
<meta charset="utf-8">
<title>Bright Ridge Pest Control – Business Cards</title>
<link href="https://fonts.googleapis.com/css2?family=Open+Sans:ital,wght@0,400;0,600;0,700;0,800;1,600&display=swap" rel="stylesheet">
<style>
  :root {
    --orange: #ee7324;
    --black: #0d0d0d;
    --white: #ffffff;
    --paper-bg: #2a2d31;
    --text: #111111;
  }
  * { box-sizing: border-box; margin: 0; padding: 0; }
  html, body { width: 1200px; height: 900px; overflow: hidden; }
  body {
    background: var(--paper-bg);
    font-family: "Open Sans", Arial, sans-serif;
    position: relative;
  }
  .card {
    position: absolute;
    width: 640px;
    height: 366px;
    background: var(--white);
    overflow: hidden;
    box-shadow: 0 10px 30px rgba(0,0,0,.45);
  }
  .card--front { left: 500px; top: 50px; }
  .card--back { left: 60px; top: 480px; }

  /* Front */
  .front__top-band {
    position: absolute; left: 0; top: 0; width: 100%; height: 16px;
    background: var(--orange);
  }
  .brand {
    position: absolute; left: 170px; top: 70px; width: 440px;
    display: flex; align-items: center; gap: 14px;
  }
  .brand__mark { width: 30px; height: 30px; background: var(--orange); flex: none; }
  .brand__name {
    color: var(--orange); font-weight: 800; font-size: 46px;
    line-height: 1; letter-spacing: 1px; text-transform: uppercase;
  }
  .brand__tagline {
    position: absolute; left: 214px; top: 128px;
    color: var(--orange); font-weight: 800; font-size: 18px;
    letter-spacing: 14px; text-transform: uppercase;
  }
  .owner-tab {
    position: absolute; left: 0; top: 180px; width: 330px; height: 46px;
    background: var(--orange);
    clip-path: polygon(0 0, 100% 0, 92% 100%, 0 100%);
    color: var(--white); font-style: italic; font-weight: 600; font-size: 22px;
    display: flex; align-items: center; padding-left: 30px;
  }
  .phone-bar {
    position: absolute; right: 0; top: 236px; width: 360px; height: 52px;
    background: var(--black);
    clip-path: polygon(7% 0, 100% 0, 100% 100%, 0 100%);
    color: var(--white); font-weight: 700; font-size: 28px;
    display: flex; align-items: center; gap: 12px; padding-left: 52px;
  }
  .phone-bar svg { width: 24px; height: 24px; fill: var(--white); flex: none; }
  .email {
    position: absolute; right: 30px; top: 300px;
    font-weight: 600; font-size: 15px; color: var(--text);
    text-transform: uppercase; letter-spacing: .3px;
  }
  .front__bottom-band {
    position: absolute; left: 0; bottom: 0; width: 100%; height: 20px;
    background: var(--black);
  }

  /* Back */
  .services-tab {
    position: absolute; left: 0; top: 26px; width: 440px; height: 50px;
    background: var(--orange);
    clip-path: polygon(0 0, 100% 0, 94% 100%, 0 100%);
    color: var(--white); font-weight: 700; font-size: 26px;
    display: flex; align-items: center; padding-left: 38px;
  }
  .services-slashes {
    position: absolute; left: 436px; top: 26px; width: 40px; height: 50px;
  }
  .service-list {
    position: absolute; list-style: none;
    font-weight: 700; font-size: 21px; line-height: 31px; color: var(--text);
  }
  .service-list--left { left: 52px; top: 96px; }
  .service-list--right { left: 390px; top: 150px; }
  .divider { position: absolute; left: 250px; top: 130px; width: 120px; height: 150px; }
  .web-band {
    position: absolute; left: 0; bottom: 0; width: 100%; height: 44px;
    background: var(--black);
    color: var(--white); font-weight: 600; font-size: 21px;
    display: flex; align-items: center; padding-left: 44px;
  }
</style>
</head>
<body>
  <section class="card card--front" aria-label="Business card front">
    <div class="front__top-band"></div>
    <div class="brand">
      <span class="brand__mark"></span>
      <span class="brand__name">Bright Ridge</span>
    </div>
    <div class="brand__tagline">Pest Control</div>
    <div class="owner-tab">Sam Porter (owner)</div>
    <div class="phone-bar">
      <svg viewBox="0 0 24 24" aria-hidden="true"><path d="M6.6 10.8a15.1 15.1 0 0 0 6.6 6.6l2.2-2.2a1 1 0 0 1 1-.25 11.4 11.4 0 0 0 3.6.57 1 1 0 0 1 1 1V20a1 1 0 0 1-1 1A17 17 0 0 1 3 4a1 1 0 0 1 1-1h3.5a1 1 0 0 1 1 1c0 1.25.2 2.45.57 3.57a1 1 0 0 1-.25 1z"/></svg>
      <span>555-014-2870</span>
    </div>
    <div class="email">sam@brightridgepest.com</div>
    <div class="front__bottom-band"></div>
  </section>

  <section class="card card--back" aria-label="Business card back">
    <div class="services-tab">Services / Inspections</div>
    <svg class="services-slashes" viewBox="0 0 40 50" aria-hidden="true">
      <polygon points="14,0 22,0 8,50 0,50" fill="var(--orange)"/>
      <polygon points="30,0 38,0 24,50 16,50" fill="var(--orange)"/>
    </svg>
    <ol class="service-list service-list--left">
      <li>1. Ants</li>
      <li>2. Mosquitos</li>
      <li>3. Fleas</li>
      <li>4. Roaches</li>
      <li>5. Stinging Insects</li>
    </ol>
    <svg class="divider" viewBox="0 0 120 150" aria-hidden="true">
      <line x1="115" y1="5" x2="5" y2="145" stroke="var(--black)" stroke-width="2"/>
    </svg>
    <ol class="service-list service-list--right">
      <li>6. Spiders</li>
      <li>7. Rodents</li>
      <li>8. Termites</li>
      <li>9. Mice</li>
      <li>10. Rats</li>
    </ol>
    <div class="web-band">www.brightridgepest.com</div>
  </section>
</body>
</html>
```